依頼詳細
【サイトの最大の要望】
・新規集客(ネット予約がゴール)
・院の認知アップ(新規開業のため)

【強み】
・お待たせしないシステム
・保険適用の漢方治療

【ターゲット】
・世代:30代以降
・性別:やや女性寄り

【完成イメージ】
全面は白で、植物などの緑、茶色・木目調を差し色にしています。
待合室については濃いめの木目調のカウンターテーブルがあり、
ペンダントライトでカフェ風な作りになっています。

・完成イメージ
http://vrview.mokunoie-kenchiku.jp/wt_movie/p_mv/48391qzpa7r/vtour/tour.html

・木乃家建築で内観がイメージに近い事例
http://www.mokunoie-kenchiku.jp/medical/doctor/example/morita_naika.html

【参考サイト】
https://www.kawabe-dining.jp/lavendora/
https://sorine-cafe.jp/
http://www.kirigaoka-tei.com/restaurant/wrencafe/
http://waffle.tovari-works.jp/
http://www.almondlodge.jp/#!page4

【サイトマップ】
1.TOP
2.初めての方へ
3.医院について
4.当院の特徴
5.院長紹介
6.よくある質問
7.ブログ(一覧)
∟8.ブログ(詳細)
9.お知らせ(一覧)
∟10.お知らせ(詳細)
11.耳の病気
12.鼻の病気
13.口・のどの病気
14.頭・顔・首の病気
15.風邪の症状
16.更年期の症状にお悩みの方
17.冷えにお悩みの方へ
18.不眠にお悩みの方へ
19.めまい・耳鳴りにお悩みの方へ
20.体質改善
希望イメージ
• シンプル
複雑
• 単色
カラフル
• 暗い
明るい
• 日常
高級
• 遊び心
厳粛
• 未来的
伝統的
• 女性的
男性的
希望する色
ベースは白。植物などの緑、木目調の濃い茶色を差し色
納品ファイル
• フォトショップ形式 (.psd)
• PNG形式 (.png)
補足説明
【店舗へのご連絡はおやめください】
ワークミツ規約にもありますが、店舗への通常業務に支障が出るため、
直接電話等のお問い合わせをお控え頂きますよう、ご協力願います。

【素材写真】
素材については、ピクセラのカンプ画像をご使用ください。
選定後に正規データをお渡し致します。
(画像はマンスリーパック内でお願い致します。)
依頼公開後の追記内容
ワイヤフレームを添付致します。
提案期間を延長致します。
提案数がないため、期限を延長致します。
こちら提案数が欲しいため、延長致します。
■ 選んだ理由

一見してシンプルながら目を引くデザインで、院のイメージに合っていたため

■ 提案者全員のお礼・コメント

この度はご提案くださり、ありがとうございました。
また機会がございましたら、どうぞ宜しくお願い致します。

```html
<!DOCTYPE html>
<html lang="ja">
<head>
<meta charset="utf-8">
<title>すずらん耳鼻咽喉科</title>
<link href="https://fonts.googleapis.com/css2?family=Noto+Serif+JP:wght@400;600&family=Noto+Sans+JP:wght@400;500&display=swap" rel="stylesheet">
<style>
:root{
  --green:#7fb236;
  --green-dark:#5d8f22;
  --brown:#7a5a35;
  --brown-light:#a88a62;
  --beige:#f6f2ea;
  --line:#ddd5c8;
  --text:#4a3f33;
  --muted:#8b8074;
  --white:#ffffff;
}
*{margin:0;padding:0;box-sizing:border-box}
html,body{width:1200px;height:3556px;overflow:hidden}
body{font-family:"Noto Serif JP",serif;color:var(--text);background:var(--white);position:relative;font-size:13px;line-height:1.8}
.abs{position:absolute}
.ph{position:absolute;display:block}
.sans{font-family:"Noto Sans JP",sans-serif}

/* hero */
.hero{left:0;top:0;width:1200px;height:585px;background:linear-gradient(180deg,#c9dbe8 0%,#e9eef0 45%,#d9d2c4 75%,#b9b0a2 100%)}
.brand-card{left:50px;top:22px;width:300px;height:400px;background:rgba(255,255,255,.92);padding:22px 22px}
.brand-card .kana{font-size:10px;letter-spacing:.2em;color:var(--green-dark)}
.brand-card .name{font-size:25px;color:var(--green-dark);font-weight:600;letter-spacing:.05em;display:flex;align-items:center;gap:8px}
.brand-card .name i{width:12px;height:12px;border-radius:50%;background:var(--green);display:inline-block}
.brand-card .addr{font-size:11px;color:var(--muted);margin-top:6px}
.brand-card .tel{font-size:30px;color:var(--brown);display:flex;align-items:center;gap:8px;margin:6px 0 10px;letter-spacing:.03em}
.hours{width:100%;border-collapse:collapse;font-size:11px;font-family:"Noto Sans JP",sans-serif}
.hours th,.hours td{border-bottom:1px solid var(--line);padding:6px 2px;text-align:center;font-weight:400}
.hours th:first-child,.hours td:first-child{text-align:left}
.hours td{color:var(--green-dark)}
.brand-card .note{font-size:10px;color:var(--muted);margin-top:8px}
.reserve{left:1010px;top:250px;width:140px;height:140px;border-radius:50%;background:var(--green);color:var(--white);display:flex;flex-direction:column;align-items:center;justify-content:center;font-size:19px;line-height:1.4;text-align:center;border:4px solid rgba(255,255,255,.6)}

/* nav */
.gnav{left:0;top:590px;width:1200px;height:68px;background:var(--white);border-bottom:1px solid var(--line);display:flex;justify-content:center}
.gnav a{width:128px;display:flex;align-items:center;justify-content:center;font-size:13px;color:var(--text);text-decoration:none;border-left:1px solid var(--line)}
.gnav a:last-child{border-right:1px solid var(--line)}

/* intro */
.intro{left:0;top:672px;width:1200px;height:250px;background:linear-gradient(90deg,#e4ddd1 0%,#f4f1ec 30%,#fff 60%,#f4f1ec 85%,#e2dbcf 100%)}
.intro-copy{left:0;top:705px;width:1200px;text-align:center}
.intro-copy h2{font-size:24px;font-weight:400;line-height:1.7;color:var(--brown);letter-spacing:.05em}
.intro-copy p{font-size:12px;color:var(--muted);margin-top:12px;line-height:1.9}

/* medical */
.med-main{left:0;top:940px;width:600px;height:385px;background:linear-gradient(135deg,#cfc6ba,#ece6dd 55%,#b9ab9a)}
.med-main-label{left:30px;top:1150px;font-size:34px;color:var(--brown);letter-spacing:.08em}
.ear{left:620px;top:950px;width:580px;height:150px}
.ear .img{left:0;top:0;width:250px;height:150px;background:linear-gradient(135deg,#ede8e2,#cfc7bc)}
.ear h3{left:300px;top:10px;font-size:22px;font-weight:400;color:var(--brown)}
.ear p{left:300px;top:52px;width:260px;font-size:11px;color:var(--muted)}
.sub{width:280px;height:95px;border-bottom:1px solid var(--line);display:flex;align-items:center;gap:18px}
.sub .img{width:90px;height:75px;background:linear-gradient(135deg,#e3dcd2,#c6bcae)}
.sub span{font-size:17px;color:var(--text)}

/* kampo */
.km-head{left:0;top:1345px;width:600px;height:90px;background:linear-gradient(90deg,#ede8e1,#f8f6f2)}
.km-head .img{left:0;top:0;width:160px;height:90px;background:linear-gradient(135deg,#d7cec2,#bfb2a2)}
.km-head h3{left:175px;top:8px;font-size:15px;font-weight:400;color:var(--brown)}
.km-head p{left:175px;top:36px;width:400px;font-size:10px;color:var(--muted);line-height:1.6}
.km-sub{width:280px;height:70px;display:flex;align-items:center;gap:16px}
.km-sub .img{width:80px;height:60px;background:linear-gradient(135deg,#e6dfd6,#c9bfb2)}
.km-sub span{font-size:14px;line-height:1.5}
.herb{left:610px;top:1345px;width:590px;height:240px;background:linear-gradient(135deg,#c9a97a,#a5773f 40%,#d8c08f 70%,#8b6a3c)}
.herb-label{left:650px;top:1395px;padding:8px 18px;background:rgba(255,255,255,.85);font-size:34px;color:var(--brown);letter-spacing:.08em}

/* features */
.features{left:0;top:1600px;width:1200px;height:650px;background:var(--beige)}
.sec-title{width:1200px;text-align:center;font-size:26px;font-weight:400;color:var(--brown);letter-spacing:.12em}
.sec-title:after{content:"";display:block;width:40px;height:2px;background:var(--green);margin:10px auto 0}
.feat{width:300px}
.feat .img{position:relative;width:300px;height:200px;background:linear-gradient(135deg,#e8e3dc,#c8bfb3)}
.feat .img b{position:absolute;left:14px;bottom:-30px;font-size:56px;color:var(--green);font-weight:400;font-family:"Noto Serif JP",serif;line-height:1}
.feat h4{font-size:15px;font-weight:600;color:var(--brown);margin-top:40px}
.feat p{font-size:11px;color:var(--muted);margin-top:6px;line-height:1.9}
.more{left:530px;top:2175px;width:140px;height:36px;border:1px solid var(--brown-light);display:flex;align-items:center;justify-content:center;font-size:12px;color:var(--brown);background:var(--white)}

/* director */
.director{left:0;top:2270px;width:1200px;height:420px;background:linear-gradient(90deg,#fff 0%,#fff 40%,#f1eee9 100%)}
.dir-title{left:60px;top:2300px;font-size:28px;font-weight:400;color:var(--brown);letter-spacing:.12em}
.dir-text{left:120px;top:2360px;width:420px;font-size:11px;color:var(--muted);line-height:2}
.dir-list{left:120px;top:2490px;width:420px;display:grid;grid-template-columns:1fr 1fr;gap:4px 20px;font-size:11px;list-style:none}
.dir-list li:before{content:"・";color:var(--green)}
.dir-photo{left:620px;top:2290px;width:560px;height:380px;background:linear-gradient(135deg,#dfe4e6,#f3f3f1 45%,#c9ccc8)}
.plant{left:0;top:2300px;width:100px;height:380px;background:linear-gradient(180deg,rgba(127,178,54,.15),rgba(127,178,54,.35))}

/* news & blog */
.box-head{height:44px;border-bottom:2px solid var(--green);display:flex;align-items:center;justify-content:space-between}
.box-head h3{font-size:17px;font-weight:400;color:var(--brown);display:flex;align-items:center;gap:8px}
.box-head h3 i{width:8px;height:8px;background:var(--green);display:inline-block}
.box-head span{font-size:11px;border:1px solid var(--line);padding:2px 12px;color:var(--muted)}
.news{left:60px;top:2720px;width:520px}
.news li{list-style:none;display:flex;gap:18px;font-size:11px;padding:12px 0;border-bottom:1px dotted var(--line)}
.news time{color:var(--green-dark);width:80px;flex:none}
.blog{left:620px;top:2720px;width:520px}
.blog .img{position:absolute;left:0;top:62px;width:170px;height:120px;background:linear-gradient(135deg,#e7e2db,#c9c0b4)}
.blog time{position:absolute;left:190px;top:62px;font-size:11px;color:var(--green-dark)}
.blog h4{position:absolute;left:190px;top:84px;font-size:17px;font-weight:600;color:var(--brown)}
.blog p{position:absolute;left:190px;top:118px;width:330px;font-size:11px;color:var(--muted)}

/* map */
.map{left:0;top:3060px;width:1200px;height:360px;background:linear-gradient(135deg,#eceae5,#e2e0da 50%,#ecebe6)}

/* footer */
.fnav{left:0;top:3430px;width:1200px;height:95px;display:flex;justify-content:center;gap:20px}
.fnav ul{list-style:none;width:150px;font-size:11px;line-height:1.9}
.fnav li:before{content:"› ";color:var(--green)}
.copy{left:0;top:3528px;width:1200px;height:28px;background:var(--green);color:var(--white);font-size:10px;display:flex;align-items:center;justify-content:center;letter-spacing:.1em}
.pagetop{left:1140px;top:3380px;width:40px;height:40px;background:var(--brown);display:flex;align-items:center;justify-content:center}
</style>
</head>
<body>

<div class="ph hero" role="img" aria-label="白い外壁と木目調の入口を持つクリニック外観写真"></div>

<div class="abs brand-card">
  <div class="kana">SUZURAN EAR NOSE &amp; THROAT CLINIC</div>
  <div class="name"><i></i>すずらん耳鼻咽喉科</div>
  <div class="addr">〒310-0000 緑ヶ丘県若葉市青葉町1-2-3</div>
  <div class="tel">
    <svg width="24" height="24" viewBox="0 0 24 24"><path d="M6.6 10.8a15 15 0 006.6 6.6l2.2-2.2a1 1 0 011-.25 11.4 11.4 0 003.6.6 1 1 0 011 1V20a1 1 0 01-1 1A17 17 0 013 4a1 1 0 011-1h3.5a1 1 0 011 1c0 1.25.2 2.45.6 3.6a1 1 0 01-.25 1z" fill="#7a5a35"/></svg>
    029-000-4817
  </div>
  <table class="hours">
    <tr><th>診療時間</th><th>月</th><th>火</th><th>水</th><th>木</th><th>金</th><th>土</th><th>日</th></tr>
    <tr><td>9:00-12:30</td><td>●</td><td>●</td><td>●</td><td>／</td><td>●</td><td>●</td><td>／</td></tr>
    <tr><td>15:00-18:30</td><td>●</td><td>●</td><td>●</td><td>／</td><td>●</td><td>▲</td><td>／</td></tr>
  </table>
  <div class="note sans">休診日：木曜・日曜・祝日　▲土曜午後は17:00まで</div>
</div>

<div class="abs reserve">ご予約は<br>こちら
  <svg width="18" height="10" viewBox="0 0 18 10"><path d="M1 5h15M12 1l4 4-4 4" stroke="#fff" fill="none" stroke-width="1.5"/></svg>
</div>

<nav class="abs gnav">
  <a>初めての方へ</a><a>医院について</a><a>当院の特徴</a><a>院長紹介</a><a>耳鼻咽喉科</a><a>漢方治療</a><a>お知らせ</a><a>よくある質問</a>
</nav>

<div class="ph intro" role="img" aria-label="ペンダントライトと木目のカウンターがある待合室の写真"></div>
<div class="abs intro-copy">
  <h2>患者様とのコミュニケーションを第一に考え、<br>ご要望されている治療や必要な治療に努めています。</h2>
  <p>すずらん耳鼻咽喉科では、お待たせしないシステムを導入し、<br>保険適用の漢方治療にも対応しております。どうぞお気軽にご相談ください。</p>
</div>

<div class="ph med-main" role="img" aria-label="鼻をかむ女性の写真"></div>
<div class="abs med-main-label">耳鼻咽喉科</div>

<div class="abs ear">
  <div class="ph img" role="img" aria-label="耳に手を当てる女性の写真"></div>
  <h3 class="abs">耳の病気</h3>
  <p class="abs">中耳炎や外耳炎、難聴など耳のお悩みに幅広く対応しております。お気軽にご相談ください。</p>
</div>
<div class="abs sub" style="left:620px;top:1115px"><div class="img" role="img" aria-label="鼻の病気のイメージ写真"></div><span>鼻の病気</span></div>
<div class="abs sub" style="left:910px;top:1115px"><div class="img" role="img" aria-label="口・のどの病気のイメージ写真"></div><span>口・のどの病気</span></div>
<div class="abs sub" style="left:620px;top:1215px"><div class="img" role="img" aria-label="頭・顔・首の病気のイメージ写真"></div><span>頭・顔・首の病気</span></div>
<div class="abs sub" style="left:910px;top:1215px"><div class="img" role="img" aria-label="風邪の症状のイメージ写真"></div><span>風邪の症状</span></div>

<div class="abs km-head">
  <div class="ph img" role="img" aria-label="更年期に悩む女性の写真"></div>
  <h3 class="abs">更年期の症状にお悩みの方へ</h3>
  <p class="abs">ほてりやのぼせ、気分の落ち込みなど、更年期の不調に漢方でやさしく寄り添います。</p>
</div>
<div class="abs km-sub" style="left:10px;top:1442px"><div class="img" role="img" aria-label="冷えのイメージ写真"></div><span>冷えに<br>お悩みの方へ</span></div>
<div class="abs km-sub" style="left:300px;top:1442px"><div class="img" role="img" aria-label="不眠のイメージ写真"></div><span>不眠に<br>お悩みの方へ</span></div>
<div class="abs km-sub" style="left:10px;top:1515px"><div class="img" role="img" aria-label="めまい・耳鳴りのイメージ写真"></div><span>めまい・耳鳴りに<br>お悩みの方へ</span></div>
<div class="abs km-sub" style="left:300px;top:1515px"><div class="img" role="img" aria-label="体質改善のイメージ写真"></div><span>体質改善</span></div>

<div class="ph herb" role="img" aria-label="器に盛られた生薬の写真"></div>
<div class="abs herb-label">漢方治療</div>

<div class="ph features" role="img" aria-label="淡いベージュの背景"></div>
<h2 class="abs sec-title" style="left:0;top:1630px">当院の特徴</h2>
<div class="abs feat" style="left:120px;top:1720px">
  <div class="img" role="img" aria-label="医師が患者に説明する写真"><b>01</b></div>
  <h4>お待たせしないシステム</h4>
  <p>ネット予約と順番管理で待ち時間を短縮。ご自宅で順番をお待ちいただけます。</p>
</div>
<div class="abs feat" style="left:450px;top:1720px">
  <div class="img" role="img" aria-label="生薬が並ぶ写真"><b>02</b></div>
  <h4>保険適用の漢方治療</h4>
  <p>体質に合わせた漢方薬を保険診療でご提案。長引く不調にも対応します。</p>
</div>
<div class="abs feat" style="left:780px;top:1720px">
  <div class="img" role="img" aria-label="明るい診察室の写真"><b>03</b></div>
  <h4>落ち着いた院内空間</h4>
  <p>木目と緑を基調としたカフェのような空間で、リラックスしてお過ごしください。</p>
</div>
<div class="abs more">詳しくはこちら</div>

<div class="ph director" role="img" aria-label="白い背景"></div>
<div class="ph plant" role="img" aria-label="観葉植物の写真"></div>
<h2 class="abs dir-title">院長紹介</h2>
<p class="abs dir-text">地域の皆様に寄り添い、どんな小さなお悩みにも耳を傾ける診療を心がけております。耳・鼻・のどの症状はもちろん、漢方を取り入れた体にやさしい治療で、皆様の健康を支えてまいります。</p>
<ul class="abs dir-list">
  <li>医学博士</li><li>日本耳鼻咽喉科学会 専門医</li>
  <li>大学病院 耳鼻咽喉科 勤務</li><li>総合病院 耳鼻咽喉科 医長</li>
  <li>漢方外来 担当医</li><li>2018年 当院開院</li>
</ul>
<div class="ph dir-photo" role="img" aria-label="パソコンに向かう白衣の院長の写真"></div>

<section class="abs news">
  <div class="box-head"><h3><i></i>すずらん耳鼻咽喉科からのお知らせ</h3><span>一覧はこちら</span></div>
  <ul>
    <li><time>2018.04.10</time>年末年始の休診日についてのお知らせを掲載しました。</li>
    <li><time>2018.03.22</time>インフルエンザ予防接種の受付を開始いたしました。</li>
    <li><time>2018.02.15</time>ホームページを公開いたしました。</li>
    <li><time>2018.01.30</time>ネット予約システムの運用を開始しました。</li>
  </ul>
</section>

<section class="abs blog">
  <div class="box-head"><h3><i></i>医療ブログ</h3><span>一覧はこちら</span></div>
  <div class="img" role="img" aria-label="ブログ記事のサムネイル写真"></div>
  <time>2018.04.12</time>
  <h4>花粉症の季節のセルフケア</h4>
  <p>春先に増える鼻水やくしゃみ。毎日の生活で気をつけたいポイントをご紹介します。</p>
</section>

<div class="ph map" role="img" aria-label="クリニック周辺の地図"></div>
<svg class="abs" style="left:640px;top:3200px" width="40" height="54" viewBox="0 0 40 54"><path d="M20 2C10 2 3 9 3 19c0 13 17 33 17 33s17-20 17-33C37 9 30 2 20 2z" fill="#7fb236"/><circle cx="20" cy="19" r="7" fill="#fff"/></svg>
<div class="abs pagetop"><svg width="16" height="10" viewBox="0 0 16 10"><path d="M1 9l7-7 7 7" stroke="#fff" fill="none" stroke-width="1.5"/></svg></div>

<footer class="abs fnav sans">
  <ul><li>初めての方へ</li><li>医院について</li><li>当院の特徴</li><li>院長紹介</li></ul>
  <ul><li>よくある質問</li><li>お知らせ</li><li>医療ブログ</li></ul>
  <ul><li>耳の病気</li><li>鼻の病気</li><li>口・のどの病気</li><li>頭・顔・首の病気</li></ul>
  <ul><li>風邪の症状</li><li>漢方治療</li><li>体質改善</li></ul>
  <ul><li>更年期の症状にお悩みの方へ</li><li>冷えにお悩みの方へ</li><li>不眠にお悩みの方へ</li><li>めまい・耳鳴りにお悩みの方へ</li></ul>
</footer>
<div class="abs copy sans">© すずらん耳鼻咽喉科 All Rights Reserved.</div>

</body>
</html>
```